Inspirational Quote Poster for Employees

For this project, we need a simple yet high-impact poster template that will be customized for each of our employees with a personalized inspirational quote and color scheme. This template should allow us to quickly and easily customize the text and colors in the poster without a lot of effort.

The poster design should consist of:
- A stylized text area to contain the main text of the quote
- A separate text area to contain the source of quote
- A background that complements the color and style of the text

Text may use different typographic effects (such as color, stroke weight, italicization, font size changes, drop shadows) to draw attention to words in the quote; the source of the quote may be formatted the same as the main text of the quote, or may be formatted differently to distinguish it from the main quote.

The background may be simply a single color, subtle texture, gradients, halftone effects, or other color/texture effects may be used to complement the text.

Examples of the types of posters envisioned by this project:
- http://www.pinvelora.example/marcusdtelford/quillbase-job-1/

Sample quotes to use to build your poster - choose whichever one you want, but be certain that the poster design will handle both long and short quotes:
- "Happiness in intelligent people is the rarest thing I know" - Walden Prosket
- "Wanting to be someone else is a waste of the person you are." - Rolf Dintey
- "Experience is not what happens to you. It is what you do with what happens to you." - Ferris Mundell
- "Simplicity is the ultimate in sophistication." - Rinaldo de Pavesco
- "You will get all you want in life if you help enough other people get what they want." - Tad Pomfrey
- "Hell, there are no rules here — we're trying to accomplish something." - Gareth Vullane

Industry/Entity Type

Quote

Requirements
Must have
• Final deliverable must be:
• - Formatted for an 18” x 24” poster (in portrait orientation)
• - Delivered in Adobe InDesign, Adobe Illustrator, or Extended PostScript format
• - Use CMYK color mode
• - Be print-ready at 300dpi resolution
• - Include any fonts used in the template

```html
<!DOCTYPE html>
<html lang="en">
<head>
<meta charset="utf-8">
<title>Quote Poster – Ferris Mundell</title>
<link rel="stylesheet" href="https://fonts.googleapis.com/css2?family=Cinzel:wght@400&family=Ropa+Sans&display=swap">
<style>
  :root {
    --paper-light: #ffffff;
    --paper-yellow: #fffb00;
    --rust: #bd5316;
    --ink-light: #ffffff;
    --photo-top: rgba(150, 120, 100, 0.55);
    --photo-mid: rgba(205, 140, 70, 0.5);
    --photo-low: rgba(255, 235, 90, 0);
  }
  * { margin: 0; padding: 0; box-sizing: border-box; }
  html, body {
    width: 848px;
    height: 1200px;
    overflow: hidden;
  }
  .poster {
    position: relative;
    width: 848px;
    height: 1200px;
    overflow: hidden;
    background: linear-gradient(160deg, var(--paper-light) 0%, #fffdd0 22%, #fffb55 45%, var(--paper-yellow) 70%);
  }
  .portrait {
    position: absolute;
    left: 80px;
    top: 18px;
    width: 610px;
    height: 665px;
    background: linear-gradient(180deg, var(--photo-top) 0%, var(--photo-mid) 55%, var(--photo-low) 100%);
  }
  .quote {
    position: absolute;
    left: 0;
    top: 690px;
    width: 848px;
    text-align: center;
    font-family: "Cinzel", "Trajan Pro", serif;
    font-size: 76px;
    color: var(--ink-light);
  }
  .quote-line {
    display: block;
    height: 68.5px;
  }
  .quote-line span {
    display: inline-block;
    background: var(--rust);
    padding: 0 12px;
    height: 70px;
    line-height: 84px;
    white-space: nowrap;
    letter-spacing: -1px;
  }
  .source-rule {
    position: absolute;
    left: 108px;
    top: 1040px;
    width: 632px;
    height: 12px;
  }
  .source {
    position: absolute;
    left: 0;
    top: 1054px;
    width: 848px;
    text-align: center;
    font-family: "Ropa Sans", "Arial Narrow", sans-serif;
    font-size: 50px;
    line-height: 54px;
    color: var(--rust);
    letter-spacing: -1.5px;
  }
</style>
</head>
<body>
  <main class="poster">
    <div class="portrait" role="img" aria-label="Photo placeholder: warm-toned portrait of the quote's author"></div>

    <blockquote class="quote">
      <span class="quote-line"><span>EXPERIENCE IS NOT</span></span>
      <span class="quote-line"><span>WHAT HAPPENS TO</span></span>
      <span class="quote-line"><span>YOU. IT IS WHAT YOU</span></span>
      <span class="quote-line"><span>DO WITH WHAT</span></span>
      <span class="quote-line"><span>HAPPENS TO YOU.</span></span>
    </blockquote>

    <svg class="source-rule" viewBox="0 0 632 12" aria-hidden="true">
      <line x1="12" y1="6" x2="620" y2="6" stroke="#bd5316" stroke-width="1.5"/>
      <circle cx="2.5" cy="6" r="2" fill="#bd5316"/>
      <circle cx="629.5" cy="6" r="2" fill="#bd5316"/>
    </svg>

    <p class="source">FERRIS MUNDELL</p>
  </main>
</body>
</html>
```